BrambleWorks business card

Looking for business card design that supports our company/software values. We have 2 logo designs at the moment but open to change if you think you can enhance the brand. Check out website www.brambleworks.com.au.

Target Market(s)

Education

Contact Information for Business Card

Name, title, mobile, email and website

Font styles to use
Sans Serif

Colors

Designer to choose colors to be used in the design.

Requirements
Must have
• BrambleWorks logo with tree and tagline on rear side with dark grey background colour

```html
<!DOCTYPE html>
<html lang="en">
<head>
<meta charset="UTF-8">
<title>BrambleWorks business card</title>
<link href="https://fonts.googleapis.com/css2?family=Montserrat:wght@400;500;600&display=swap" rel="stylesheet">
<style>
  :root {
    --backdrop: #1a1a1a;
    --card: #2a2a2a;
    --card-edge: #333333;
    --silver: #c9c9c9;
    --white: #f2f2f2;
    --gold: #f4b42a;
    --muted: #d8d8d8;
  }
  * { margin: 0; padding: 0; box-sizing: border-box; }
  html, body {
    width: 1200px; height: 900px; overflow: hidden;
    background: var(--backdrop);
    font-family: "Montserrat", sans-serif;
  }
  .canvas {
    position: relative; width: 1200px; height: 900px;
    display: flex; flex-direction: column; align-items: center; justify-content: center; gap: 28px;
  }
  .card {
    position: relative; width: 700px; height: 400px;
    background: var(--card);
    border: 1px solid var(--card-edge);
    box-shadow: 0 10px 30px rgba(0,0,0,0.5);
  }
  .card-front {
    display: flex; align-items: center; justify-content: center;
  }
  .front-mark {
    font-size: 58px; font-weight: 500; color: var(--silver); letter-spacing: 0.5px;
  }
  .card-back {
    display: flex; align-items: center; padding: 0 40px 0 48px;
  }
  .brand {
    display: flex; align-items: center; gap: 16px; width: 300px;
  }
  .brand-dot {
    width: 58px; height: 58px; border-radius: 50%; background: var(--white); flex: none;
  }
  .brand-name {
    font-size: 31px; font-weight: 500; color: var(--white); line-height: 1.1;
    padding-bottom: 6px; border-bottom: 1px solid var(--white);
  }
  .brand-tagline {
    font-size: 13px; color: var(--white); margin-top: 5px; letter-spacing: 0.3px;
  }
  .divider {
    width: 2px; height: 180px; background: var(--gold); margin: 0 30px 0 34px;
  }
  .contact { color: var(--muted); }
  .contact-name {
    font-size: 25px; font-weight: 600; color: var(--gold); letter-spacing: 1.5px; text-transform: uppercase;
  }
  .contact-title { font-size: 15px; color: var(--white); margin-bottom: 14px; }
  .contact-address { font-size: 15px; line-height: 1.45; margin-bottom: 8px; color: var(--white); }
  .contact-line {
    display: flex; align-items: center; gap: 10px; font-size: 15px; line-height: 1.7; color: var(--white);
  }
  .contact-line svg { width: 12px; height: 12px; flex: none; }
</style>
</head>
<body>
<main class="canvas">
  <section class="card card-front">
    <span class="front-mark">BrambleWorks</span>
  </section>

  <section class="card card-back">
    <div class="brand">
      <span class="brand-dot"></span>
      <div>
        <div class="brand-name">BrambleWorks</div>
        <div class="brand-tagline">Student Success Platform</div>
      </div>
    </div>
    <div class="divider"></div>
    <div class="contact">
      <div class="contact-name">Daniel Hartley</div>
      <div class="contact-title">Director</div>
      <div class="contact-address">1280 Fernhill Lane<br>Riverton, MO 65410</div>
      <div class="contact-line">
        <svg viewBox="0 0 12 12" aria-hidden="true"><path d="M3 1 L5 3.5 L4 5 Q5 7 7 8 L8.5 7 L11 9 L9.5 11 Q4 10.5 1 3 Z" fill="none" stroke="var(--gold)" stroke-width="1.2"/></svg>
        555-014-2873
      </div>
      <div class="contact-line">
        <svg viewBox="0 0 12 12" aria-hidden="true"><rect x="1" y="2.5" width="10" height="7" fill="none" stroke="var(--gold)" stroke-width="1.2"/><path d="M1 2.5 L6 6.5 L11 2.5" fill="none" stroke="var(--gold)" stroke-width="1.2"/></svg>
        info@brambleworks.com.au
      </div>
      <div class="contact-line">
        <svg viewBox="0 0 12 12" aria-hidden="true"><circle cx="6" cy="6" r="5" fill="none" stroke="var(--gold)" stroke-width="1.1"/><ellipse cx="6" cy="6" rx="2.2" ry="5" fill="none" stroke="var(--gold)" stroke-width="1"/><path d="M1 6 H11" stroke="var(--gold)" stroke-width="1"/></svg>
        www.brambleworks.com.au
      </div>
    </div>
  </section>
</main>
</body>
</html>
```